wooden jewelry - pearl necklaces

I sell wooden jeweler (rings and pearls) on markets, and so on. I also opened my business as a carpenter. The rings and a combination of wood and metal. The wood is special wood, not very common on Europe. I paint the rings afterwards. You can see some of the pictures on the pictures I uploaded. The pearls are made of the same kind of wood and colored in all kinds of colors. They are then assembled to bracelets. The jewelry is very individual and looks really cool and all kinds of people.

Target Market(s)

Young urban alternative with a sense of individuality

Contact Information for Business Card

Front:

Text:

„Kugelwerk“ (big)
„Malte Oswitz“ (smaler)

Back
„Holzschmuck
Herstellung von individuellem Holz- und Modeschmuck

Malte Oswitz
Tel: 015239460518
Lindgarbweg 9
83127 Auental

malteoswitz@postfeld.de“

Font styles to use
Sans Serif

Requirements
Nice to have
• Nice to see a camel thorn tree on the background, this is a special wood and some of the rings are made out of this wood.

```html
<!DOCTYPE html>
<html lang="de">
<head>
<meta charset="utf-8">
<title>Kugelwerk – Visitenkarte</title>
<link rel="stylesheet" href="https://fonts.googleapis.com/css2?family=Open+Sans:wght@600;700;800&display=swap">
<style>
  :root {
    --page: #ece8e2;
    --maroon: #4a0c18;
    --brick: #9b2f28;
    --mint: #86bba1;
    --mint-light: #d4e6dc;
    --white: #ffffff;
    --bead-dark: #2b1f3a;
    --bead-warm: #b8893e;
  }
  * { box-sizing: border-box; margin: 0; padding: 0; }
  html, body { width: 1200px; height: 1200px; overflow: hidden; }
  body {
    background: var(--page);
    font-family: "Open Sans", sans-serif;
    color: var(--white);
    display: flex;
    flex-direction: column;
    align-items: center;
    justify-content: center;
    gap: 60px;
  }
  .card {
    position: relative;
    width: 900px;
    height: 520px;
    overflow: hidden;
    box-shadow: 0 6px 18px rgba(0,0,0,.18);
  }

  /* Front */
  .card-front__photo {
    position: absolute; inset: 0;
    background:
      radial-gradient(circle at 20% 30%, rgba(200,170,90,.8), transparent 35%),
      radial-gradient(circle at 70% 25%, rgba(142,42,42,.7), transparent 30%),
      radial-gradient(circle at 80% 75%, rgba(43,31,58,.9), transparent 40%),
      radial-gradient(circle at 35% 80%, rgba(184,137,62,.8), transparent 40%),
      linear-gradient(135deg, var(--bead-dark), var(--bead-warm) 55%, var(--bead-dark));
  }
  .card-front__band {
    position: absolute; left: 0; right: 0; top: 200px; height: 150px;
    background: rgba(30,20,40,.25);
  }
  .card-front__brand {
    position: absolute; left: 170px; top: 215px;
  }
  .brand-name {
    font-weight: 800;
    font-size: 96px;
    letter-spacing: 2px;
    line-height: 1;
    text-transform: uppercase;
  }
  .brand-owner {
    font-weight: 700;
    font-size: 48px;
    margin: 6px 0 0 160px;
    line-height: 1.1;
  }

  /* Back */
  .card-back__shapes { position: absolute; inset: 0; }
  .card-back__head {
    position: absolute; left: 50px; top: 30px;
  }
  .label-title { font-weight: 700; font-size: 30px; letter-spacing: .5px; }
  .label-sub { font-weight: 700; font-size: 25px; margin-top: 2px; }
  .owner-name { font-weight: 700; font-size: 46px; margin-top: 14px; }
  .contact {
    position: absolute; left: 50px; top: 245px;
    font-weight: 700; font-size: 28px; line-height: 50px;
  }
  .contact__phone { display: flex; align-items: center; gap: 20px; }
  .email {
    position: absolute; left: 270px; top: 455px;
    display: flex; align-items: center; gap: 30px;
    font-weight: 700; font-size: 27px;
  }
</style>
</head>
<body>

  <section class="card card-front">
    <div class="card-front__photo" role="img" aria-label="Nahaufnahme bunter, bemalter Holzperlen"></div>
    <div class="card-front__band"></div>
    <div class="card-front__brand">
      <h1 class="brand-name">Kugelwerk</h1>
      <p class="brand-owner">Malte Oswitz</p>
    </div>
  </section>

  <section class="card card-back">
    <svg class="card-back__shapes" width="900" height="520" viewBox="0 0 900 520">
      <defs>
        <radialGradient id="treeGlow" cx="50%" cy="45%" r="55%">
          <stop offset="0" stop-color="#d4e6dc"/>
          <stop offset="1" stop-color="#d4e6dc" stop-opacity="0"/>
        </radialGradient>
        <linearGradient id="ringTone" x1="0" y1="0" x2="1" y2="1">
          <stop offset="0" stop-color="#c98a4a"/>
          <stop offset=".5" stop-color="#8a4420"/>
          <stop offset="1" stop-color="#b7b7b7"/>
        </linearGradient>
      </defs>
      <rect class="band-top" x="0" y="0" width="900" height="180" fill="var(--maroon)"/>
      <rect class="band-mint" x="0" y="180" width="900" height="260" fill="var(--mint)"/>
      <rect class="band-bottom" x="0" y="440" width="900" height="80" fill="var(--maroon)"/>

      <ellipse role="img" aria-label="Silhouette eines Kameldornbaums" cx="610" cy="300" rx="260" ry="120" fill="url(#treeGlow)"/>
      <rect role="img" aria-label="Foto zweier Ringe aus Holz und Metall" x="690" y="210" width="140" height="210" rx="50" fill="url(#ringTone)"/>

      <polygon class="wedge-wide" points="0,0 120,0 440,520 0,520" fill="var(--brick)" opacity=".55"/>
      <polygon class="wedge-narrow" points="0,0 40,0 210,520 0,520" fill="var(--brick)" opacity=".75"/>
    </svg>

    <div class="card-back__head">
      <p class="label-title">HOLZSCHMUCK</p>
      <p class="label-sub">Herstellung von individuellem Holz- und Modeschmuck</p>
      <h2 class="owner-name">Malte Oswitz</h2>
    </div>

    <div class="contact">
      <p class="contact__phone">
        <svg width="24" height="44" viewBox="0 0 24 44" aria-hidden="true">
          <rect x="2" y="2" width="20" height="40" rx="3" fill="none" stroke="#fff" stroke-width="3"/>
          <line x1="8" y1="36" x2="16" y2="36" stroke="#fff" stroke-width="3"/>
        </svg>
        015239460518
      </p>
      <p>Lindgarbweg 9</p>
      <p>83127 Auental</p>
    </div>

    <div class="email">
      <svg width="52" height="36" viewBox="0 0 52 36" aria-hidden="true">
        <rect x="2" y="2" width="48" height="32" fill="none" stroke="#fff" stroke-width="3"/>
        <polyline points="2,2 26,22 50,2" fill="none" stroke="#fff" stroke-width="3"/>
        <line x1="2" y1="34" x2="20" y2="17" stroke="#fff" stroke-width="3"/>
        <line x1="50" y1="34" x2="32" y2="17" stroke="#fff" stroke-width="3"/>
      </svg>
      <span>malteoswitz@postfeld.de</span>
    </div>
  </section>

</body>
</html>
```